VORNIK Lab Feel your information

VORNIK Lab is a soci% 26 # 233; t% 26 # 233; of mobile application design and multiexperience destiny% 26 # 233; % 26 # 224; The% 26 # 39; industry and particularly the watch industry% 26 # 232; re. By multiexperience, I mean applications usable on watches,% 26 # 233; holographic screens,% 26 # 233; touch screens g% 26 # 233; ant, r% 26 # 233; alit% 26 # 233; virtual,% 26 # 224; distance with a driftgrip and% 26 # 233; obviously on mobile on tablet and smartphone. Applications will call% 26 # 224; 3d, artificial intelligence, big data. The company logo% 26 # 233; t% 26 # 233; is attached% 26 # 233; below.

Target Market(s)

Swiss precision industry Watchmaking industry% 26 # 232; re

Coding

Coded - Design and coding required

Font styles to use
Sans Serif

Colors

Designer to choose colors to be used in the design.

Requirements
Must have
• A Contact form A gallery of Vid% 26 # 233; o / Photo (portfolio) 3D images of% 26 # 39; illustration orient% 26 # 233; es industry but% 26 # 233; also luxury (take free images A partner page
Nice to have
• A blog
Should not have
• The designs are too loaded, the page should load quickly.

```html
<!DOCTYPE html>
<html lang="en">
<head>
<meta charset="utf-8">
<title>VORNIK Lab — Feel your information</title>
<link href="https://fonts.googleapis.com/css2?family=Michroma&family=Montserrat:wght@400;500;600;700&display=swap" rel="stylesheet">
<style>
:root{
  --blue:#0a6cc0;
  --blue-dark:#0655a0;
  --navy:#1b1838;
  --ink:#222;
  --text:#555;
  --muted:#777;
  --line:#dcdcdc;
  --white:#fff;
  --deep:#0b1626;
}
*{margin:0;padding:0;box-sizing:border-box}
html,body{width:1200px;height:4637px;overflow:hidden}
body{position:relative;font-family:'Montserrat',sans-serif;color:var(--text);background:var(--white)}
section,header,footer{position:absolute;left:0;width:1200px}
.heading{font-family:'Michroma',sans-serif;font-weight:400;color:var(--navy);text-transform:uppercase;letter-spacing:2px}
.heading span{color:var(--blue)}
.btn{position:absolute;display:flex;align-items:center;justify-content:center;gap:10px;height:54px;border-radius:28px;color:#fff;font-weight:700;font-size:17px;text-decoration:none}
.btn i{width:17px;height:17px;border-radius:50%;background:#fff;display:inline-flex;align-items:center;justify-content:center}
.btn i::after{content:"";border-left:6px solid var(--blue);border-top:4px solid transparent;border-bottom:4px solid transparent;margin-left:2px}
.btn-blue{background:var(--blue)}
.btn-dark{background:var(--navy)}
.btn-dark i::after{border-left-color:var(--navy)}
.brand{font-family:'Montserrat',sans-serif;font-weight:700;color:var(--blue);display:flex;align-items:center;gap:10px;letter-spacing:1px}
.brand b{display:block;background:var(--blue)}

/* header */
.site-header{top:0;height:112px;border-bottom:1px solid #eee}
.site-header .brand{position:absolute;left:90px;top:36px;font-size:26px}
.site-header .brand b{width:22px;height:22px}
.nav{position:absolute;left:297px;top:46px;display:flex;gap:29px;font-size:16px;color:#333}
.nav .active{color:var(--blue);position:relative}
.nav .active::after{content:"";position:absolute;left:0;right:0;top:60px;height:3px;background:var(--blue)}
.call{position:absolute;left:918px;top:32px;display:flex;gap:10px;align-items:center}
.call p{font-size:17px;color:#333;line-height:1.2}
.call strong{color:var(--blue);font-size:18px}

/* hero */
.hero{top:112px;height:716px;overflow:hidden}
.hero-photo{position:absolute;inset:0;background:linear-gradient(100deg,#5a5e60 0%,#7b7f80 40%,#a7a9ab 62%,#cfcfd1 80%,#9c8a6d 100%)}
.hero svg{position:absolute;left:0;bottom:0}

/* welcome */
.welcome{top:880px;text-align:center}
.welcome h1{font-size:36px;margin-bottom:28px}
.welcome p{width:920px;margin:0 auto;font-size:15px;line-height:36px}
.welcome .btn-blue{left:388px;top:205px;width:206px}
.welcome .btn-dark{left:607px;top:205px;width:206px}
.rule{position:absolute;left:90px;width:1020px;height:1px;background:var(--line)}

/* applications */
.apps{top:1285px;text-align:center}
.apps h2{font-size:36px;margin-bottom:30px}
.apps>p{width:930px;margin:0 auto;font-size:15px;line-height:35px}
.card{position:absolute;width:331px;height:335px}
.card .shot{height:225px}
.card .body{position:absolute;left:17px;right:17px;top:189px;bottom:0;background:#fff;box-shadow:0 1px 6px rgba(0,0,0,.15);padding:24px 12px 0;text-align:center}
.card h3{color:var(--blue);font-size:17px;font-weight:600;margin-bottom:10px}
.card p{font-size:11.5px;line-height:25px;color:var(--muted)}
.dots{position:absolute;left:564px;top:906px;display:flex;gap:8px}
.dots span{width:18px;height:18px;border:2px solid #333;border-radius:50%}
.dots span:first-child{background:radial-gradient(#333 3px,transparent 4px)}

/* why */
.why{top:2290px;height:698px;overflow:hidden;background:linear-gradient(160deg,#0e2340,#06101e 60%,#0c1a2d)}
.why .panel{position:absolute;left:600px;top:0;width:600px;height:698px;background:linear-gradient(180deg,#0a64b4,#0754a0)}
.why svg{position:absolute;left:0;top:0}
.why .intro{position:absolute;left:90px;top:222px;width:428px;color:#e4e9f0}
.why .intro h2{color:#fff;font-size:36px;margin-bottom:28px}
.why .intro p{font-size:15px;line-height:36px;text-align:justify}
.why .intro .btn{position:relative;margin-top:24px;width:206px}
.feature{position:absolute;left:563px;width:560px;display:flex;gap:32px}
.feature .ico{flex:0 0 80px;height:80px;border-radius:50%;background:#fff;display:flex;align-items:center;justify-content:center;box-shadow:0 0 0 5px rgba(255,255,255,.25)}
.feature h3{color:#fff;font-size:22px;font-weight:600;margin:-2px 0 12px}
.feature p{color:#d6e6f7;font-size:13.5px;line-height:31px;text-align:justify}

/* about */
.about{top:3040px;height:340px}
.about .brand{position:absolute;left:120px;top:120px;font-size:68px}
.about .brand b{width:48px;height:48px}
.about .text{position:absolute;left:600px;top:0;width:510px}
.about h2{font-size:36px;margin-bottom:24px}
.about p{font-size:15px;line-height:36px;text-align:justify}
.about .btn{position:relative;margin-top:22px;width:206px}

/* contact */
.contact{top:3500px;height:480px;text-align:center}
.contact h2{font-size:36px;margin-bottom:26px}
.contact>p{width:1020px;margin:0 auto;font-size:15px;line-height:36px}
.field{position:absolute;height:40px;border:2px solid #d7d7d7;font-size:12px;color:#555;text-align:left;padding:10px 10px;display:flex;gap:6px}
.field::before{content:"";width:9px;height:9px;border-radius:2px;background:#555;margin-top:2px}
.contact .btn{left:497px;top:392px;width:206px}

/* footer */
.site-footer{top:4018px;height:619px;background:linear-gradient(180deg,#0a1a2c,#050d18)}
.site-footer svg{position:absolute;left:0;top:0}
.site-footer .brand{position:absolute;left:90px;top:260px;color:#fff;font-size:36px}
.site-footer .brand b{background:#fff;width:28px;height:28px}
.follow{position:absolute;left:830px;top:232px;display:flex;align-items:center;gap:6px;color:#fff;font-size:14px;font-weight:600}
.follow span{width:30px;height:30px;border:2px solid #fff;border-radius:50%}
.foot-rule{position:absolute;left:90px;top:316px;width:1020px;height:1px;background:#44526a}
.col{position:absolute;top:350px;color:#fff}
.col h4{font-size:17px;font-weight:600;margin-bottom:12px}
.col li{list-style:none;font-size:15px;line-height:36px}
.col.small li{font-size:13px}
.col.info li{font-size:12.5px;line-height:24px;display:flex;gap:10px;margin-bottom:12px}
.col.info li::before{content:"";flex:0 0 10px;height:10px;border-radius:50%;background:#fff;margin-top:6px}
.news input{display:block;width:277px;height:40px;border:0;padding:0 12px;font:12px 'Montserrat',sans-serif;margin-bottom:20px}
.news .btn{position:relative;height:40px;width:155px;font-size:15px}
.copy{position:absolute;left:0;width:1200px;top:4600px;text-align:center;color:#fff;font-size:12px}
</style>
</head>
<body>

<header class="site-header">
  <div class="brand"><b></b>VORNIK Lab</div>
  <nav class="nav">
    <span class="active">Home</span><span>About Us</span><span>Services</span><span>Our Clients</span><span>Our Blog</span><span>Contact Us</span>
  </nav>
  <div class="call">
    <svg width="40" height="40" viewBox="0 0 40 40"><circle cx="20" cy="20" r="18" fill="none" stroke="#0a6cc0" stroke-width="2.5"/><path d="M13 11c2-1 3 0 4 3s-1 3-1 4c1 3 3 5 6 6 1 0 1-2 4-1s4 2 3 4c-1 3-4 3-7 2-5-2-9-6-11-11-1-3 0-6 2-7z" fill="#0a6cc0"/></svg>
    <p>Call us:<br><strong>(555) 010-2040</strong></p>
  </div>
</header>

<section class="hero">
  <div class="hero-photo" role="img" aria-label="Photo of a person working on a laptop beside a chalkboard of data charts and technology icons"></div>
  <svg width="1200" height="140" viewBox="0 0 1200 140">
    <polygon points="0,140 0,138 600,58 1200,25 1200,140" fill="#fff"/>
    <polygon points="560,140 1200,12 1200,140" fill="#0a6cc0"/>
  </svg>
</section>

<section class="welcome">
  <h1 class="heading">Welcome to <span>VORNIK Lab</span></h1>
  <p>Sed ut perspiciatis unde omnis iste natus error sit voluptatem accusantium doloremque laudantium, totam rem aperiam, eaque ipsa quae ab illo inventore veritatis et quasi architecto beatae vitae dicta sunt explicabo. Nemo enim ipsam voluptatem quia voluptas sit aspernatur aut odit aut fugit, sed ratione voluptatem sequi nesciunt.</p>
  <a class="btn btn-blue">Read More <i></i></a>
  <a class="btn btn-dark">Get a Quote <i></i></a>
</section>

<div class="rule" style="top:1218px"></div>

<section class="apps">
  <h2 class="heading">Our applications <span>usable on</span></h2>
  <p>Sed ut perspiciatis unde omnis iste natus error sit voluptatem accusantium doloremque laudantium, totam rem aperiam, eaque ipsa quae ab illo inventore veritatis et quasi architecto beatae vitae dicta sunt explicabo</p>

  <div class="card" style="left:77px;top:168px"><div class="shot" role="img" aria-label="Hand touching a glowing smartwatch hologram" style="background:linear-gradient(135deg,#1a2a44,#5f7fa8 60%,#2a3040)"></div><div class="body"><h3>Watches</h3><p>Sed ut perspiciatis unde omnis iste natus error sit voluptatem accusantium doloremque laudantium eaque veritatis</p></div></div>
  <div class="card" style="left:435px;top:168px"><div class="shot" role="img" aria-label="Holographic dashboard with car and data displays" style="background:linear-gradient(135deg,#0a2740,#1e6c96 55%,#0a1c30)"></div><div class="body"><h3>Holographic Screens</h3><p>Sed ut perspiciatis unde omnis iste natus error sit voluptatem accusantium doloremque laudantium eaque veritatis</p></div></div>
  <div class="card" style="left:793px;top:168px"><div class="shot" role="img" aria-label="Hand on a large glowing touch screen" style="background:linear-gradient(135deg,#0c3a48,#2aa3b8 55%,#0a2530)"></div><div class="body"><h3>Giant Touch Screens</h3><p>Sed ut perspiciatis unde omnis iste natus error sit voluptatem accusantium doloremque laudantium eaque veritatis</p></div></div>

  <div class="card" style="left:77px;top:540px"><div class="shot" role="img" aria-label="Engineer wearing a virtual reality headset in a control room" style="background:linear-gradient(135deg,#3a4658,#8fa6bf 55%,#c9c05a)"></div><div class="body"><h3>Virtual Reality</h3><p>Sed ut perspiciatis unde omnis iste natus error sit voluptatem accusantium doloremque laudantium eaque veritatis</p></div></div>
  <div class="card" style="left:435px;top:540px"><div class="shot" role="img" aria-label="Smartphone with colourful app icons floating above it" style="background:linear-gradient(135deg,#1c1e3c,#5a4a90 50%,#c06a3a)"></div><div class="body"><h3>Mobile</h3><p>Sed ut perspiciatis unde omnis iste natus error sit voluptatem accusantium doloremque laudantium eaque veritatis</p></div></div>
  <div class="card" style="left:793px;top:540px"><div class="shot" role="img" aria-label="Student reading on a tablet in a bright cafe" style="background:linear-gradient(135deg,#d9d2c2,#a9b38a 50%,#7a6a52)"></div><div class="body"><h3>Tablet</h3><p>Sed ut perspiciatis unde omnis iste natus error sit voluptatem accusantium doloremque laudantium eaque veritatis</p></div></div>

  <div class="dots"><span></span><span></span><span></span></div>
</section>

<section class="why">
  <div class="panel"></div>
  <svg width="1200" height="698" viewBox="0 0 1200 698">
    <polygon points="0,0 1200,0 1200,40 600,50 0,106" fill="#0a6cc0"/>
    <polygon points="0,698 0,694 560,640 1200,598 1200,698" fill="#fff"/>
  </svg>
  <div class="intro" role="img" aria-label="Dark circuit board background" style="display:none"></div>
  <div class="intro">
    <h2 class="heading">Why choose <span>us</span></h2>
    <p>Sed ut perspiciatis unde omnis iste natus error sit voluptatem accusantium doloremque laudantium, totam rem aperiam, eaque ipsa quae ab illo inventore veritatis et quasi architecto beatae vitae dicta sunt explicabo</p>
    <a class="btn btn-blue">Read More <i></i></a>
  </div>
  <div class="feature" style="top:130px"><div class="ico"><svg width="40" height="40" viewBox="0 0 40 40"><circle cx="20" cy="18" r="12" fill="none" stroke="#0a6cc0" stroke-width="3"/><path d="M14 30v6M26 30v6" stroke="#0a6cc0" stroke-width="3"/></svg></div><div><h3>Lorem ipsum dolor sit amet</h3><p>Sed ut perspiciatis unde omnis iste natus error sit voluptatem accusantium doloremque laudantium, totam rem aperiam, evitae dicta sunt explicabo.</p></div></div>
  <div class="feature" style="top:307px"><div class="ico"><svg width="40" height="40" viewBox="0 0 40 40"><rect x="5" y="7" width="30" height="20" fill="none" stroke="#0a6cc0" stroke-width="3"/><path d="M20 27v6M12 34h16" stroke="#0a6cc0" stroke-width="3"/></svg></div><div><h3>Lorem ipsum dolor sit amet</h3><p>Sed ut perspiciatis unde omnis iste natus error sit voluptatem accusantium doloremque laudantium, totam rem aperiam, evitae dicta sunt explicabo.</p></div></div>
  <div class="feature" style="top:484px"><div class="ico"><svg width="40" height="40" viewBox="0 0 40 40"><rect x="13" y="10" width="14" height="14" fill="none" stroke="#0a6cc0" stroke-width="3"/><path d="M6 18l6 14h16l6-14" fill="none" stroke="#0a6cc0" stroke-width="3"/></svg></div><div><h3>Lorem ipsum dolor sit amet</h3><p>Sed ut perspiciatis unde omnis iste natus error sit voluptatem accusantium doloremque laudantium, totam rem aperiam, evitae dicta sunt explicabo.</p></div></div>
</section>

<section class="about">
  <div class="brand"><b></b>VORNIK Lab</div>
  <div class="text">
    <h2 class="heading">About <span>us</span></h2>
    <p>Sed ut perspiciatis unde omnis iste natus error sit voluptatem accusantium doloremque laudantium, totam rem aperiam, eaque ipsa quae ab illo inventore veritatis et quasi architecto beatae vitae dicta sunt explicabo. Nemo enim ipsam voluptatem quia voluptas sit aspernatur aut odit aut fugit nesciunt</p>
    <a class="btn btn-blue">Read More <i></i></a>
  </div>
</section>

<div class="rule" style="top:3434px"></div>

<section class="contact">
  <h2 class="heading">Contact <span>VORNIK Lab</span></h2>
  <p>At vero eos et accusamus et iusto odio dignissimos ducimus qui blanditiis praesentium voluptatum deleniti atque corrupti quos dolores et quas molestias excepturi sint occaecati cupiditate non provident</p>
  <div class="field" style="left:90px;top:159px;width:501px">First Name</div>
  <div class="field" style="left:610px;top:159px;width:501px">Last Name</div>
  <div class="field" style="left:90px;top:213px;width:501px">Company</div>
  <div class="field" style="left:610px;top:213px;width:501px;height:150px">Message :</div>
  <div class="field" style="left:90px;top:267px;width:501px">Email Address</div>
  <div class="field" style="left:90px;top:321px;width:501px">Phone Number</div>
  <a class="btn btn-blue">Submit <i></i></a>
</section>

<footer class="site-footer">
  <svg width="1200" height="140" viewBox="0 0 1200 140">
    <polygon points="0,0 1200,0 1200,18 0,18" fill="#fff"/>
    <polygon points="0,18 1200,18 1200,60 600,105 0,130" fill="#0a6cc0"/>
  </svg>
  <div class="brand"><b></b>VORNIK Lab</div>
  <div class="follow">FOLLOW US : <span></span><span></span><span></span><span></span><span></span></div>
  <div class="foot-rule"></div>
  <div class="col" style="left:92px"><h4>NAVIGATION</h4><ul><li>Home</li><li>About Us</li><li>Our Services</li><li>Our Blog</li><li>Reviews</li></ul></div>
  <div class="col small" style="left:330px"><h4>LINKS</h4><ul><li>Terms &amp; Conditions</li><li>Privacy Policy</li><li>Site Map</li><li>Disclaimer</li><li>Contact Us</li></ul></div>
  <div class="col info" style="left:537px;width:240px"><h4>CONTACT INFO</h4><ul><li>418 Alder Lane, Brookvale, Texas - 70001</li><li>Help : +1 555 010 2040</li><li>hello@vornik-lab.example</li></ul></div>
  <div class="col news" style="left:836px"><h4>NEWSLETTER</h4><input type="text" placeholder="Enter e-mail address"><a class="btn btn-blue">Subscribe</a></div>
</footer>
<p class="copy">Copyrights© VORNIK Lab. 2020 | Allrights Reserved.</p>

</body>
</html>
```